design a construction company business card

Design business card around our logo. Card must have all the typical info: name, title, address, phone, email, business name, etc. Somewhere on the card I would like to see our motto "Built on integrity... Inspired by commitment." Consider adding a splash of bright orange to the card to complement the blues and silvers/grays in the logo. We are open to metallic inks, textures, etc. We would like to see options on both light and dark backgrounds. The font in the logo is Euro Technic Extended Regular.

```html
<!DOCTYPE html>
<html lang="en">
<head>
<meta charset="utf-8">
<title>Halvorsen Contracting – Business Card</title>
<link href="https://fonts.googleapis.com/css2?family=Montserrat:wght@400;500&family=Open+Sans:wght@700&display=swap" rel="stylesheet">
<style>
  :root {
    --backdrop: #141414;
    --card: #26272a;
    --card-edge: #1c1d1f;
    --silver: #c9cbce;
    --text-light: #e9eaec;
    --text-muted: #a9abaf;
    --accent-blue: #1f63d6;
    --band-white: #f4f4f4;
  }
  * { margin: 0; padding: 0; box-sizing: border-box; }
  html, body {
    width: 1200px; height: 960px; overflow: hidden;
    background: var(--backdrop);
    font-family: "Montserrat", sans-serif;
  }
  .canvas {
    position: relative; width: 1200px; height: 960px;
  }
  .card {
    position: absolute;
    width: 525px; height: 300px;
    background: var(--card);
    border-radius: 4px;
    box-shadow: 0 18px 40px rgba(0,0,0,.55);
    overflow: hidden;
  }
  .card--front { left: 50px; top: 420px; }
  .card--back { left: 625px; top: 120px; }

  .wordmark {
    display: flex; align-items: center; gap: 10px;
    color: var(--silver);
    font-family: "Montserrat", sans-serif;
    font-weight: 500;
    letter-spacing: 0.04em;
  }
  .wordmark__square {
    width: 14px; height: 14px; background: var(--silver);
  }
  .card--front .wordmark { position: absolute; left: 34px; top: 38px; font-size: 19px; }

  .contact {
    position: absolute; left: 268px; top: 112px;
    color: var(--text-light);
  }
  .contact__name {
    font-family: "Open Sans", sans-serif; font-weight: 700;
    font-size: 22px; letter-spacing: 0.06em;
  }
  .contact__title { font-size: 11px; color: var(--text-muted); margin-bottom: 12px; }
  .contact__list { list-style: none; font-size: 11.5px; line-height: 18px; }
  .contact__list li { display: flex; align-items: center; gap: 8px; }
  .contact__list svg { width: 11px; height: 11px; fill: var(--text-light); flex: none; }
  .contact__address { font-size: 11.5px; margin-top: 8px; }

  .band {
    position: absolute; bottom: 12px; height: 12px;
  }
  .band--blue { left: 0; width: 248px; background: var(--accent-blue); }
  .band--white { left: 248px; right: 0; background: var(--band-white); }

  .card--back .back-content {
    position: absolute; inset: 0;
    display: flex; flex-direction: column; align-items: center; justify-content: center; gap: 20px;
  }
  .card--back .wordmark { font-size: 22px; }
  .motto { font-size: 11px; color: var(--text-muted); letter-spacing: 0.03em; }
</style>
</head>
<body>
<main class="canvas">
  <section class="card card--front" aria-label="Business card front">
    <div class="wordmark"><span class="wordmark__square"></span>Halvorsen Contracting, Inc.</div>
    <div class="contact">
      <div class="contact__name">YOUR NAME</div>
      <div class="contact__title">Your Title</div>
      <ul class="contact__list">
        <li><svg viewBox="0 0 24 24"><path d="M6.6 10.8a15 15 0 0 0 6.6 6.6l2.2-2.2a1 1 0 0 1 1-.25 11.4 11.4 0 0 0 3.6.57 1 1 0 0 1 1 1V20a1 1 0 0 1-1 1A17 17 0 0 1 3 4a1 1 0 0 1 1-1h3.5a1 1 0 0 1 1 1c0 1.25.2 2.45.57 3.57a1 1 0 0 1-.25 1z"/></svg>123-456-2100</li>
        <li><svg viewBox="0 0 24 24"><path d="M2 5h20v14H2zM4 7v.5l8 5 8-5V7z"/></svg>youremail@mailbox.com</li>
        <li><svg viewBox="0 0 24 24"><circle cx="12" cy="12" r="10"/></svg>www.yourwebsite.com</li>
      </ul>
      <div class="contact__address">Your address, city, state, ZIP 0000</div>
    </div>
    <div class="band band--blue"></div>
    <div class="band band--white"></div>
  </section>

  <section class="card card--back" aria-label="Business card back">
    <div class="back-content">
      <div class="wordmark"><span class="wordmark__square"></span>Halvorsen Contracting, Inc.</div>
      <p class="motto">Built on integrity... Inspired by commitment.</p>
    </div>
  </section>
</main>
</body>
</html>
```